Dane Morrow films- wedding and event films company website. DESKTOP AND MOBILE

We need a website for a high-end wedding and event film production company. Looking for a very modern and elegant design. my old website is www.danemorrowfilms.example

I like the "white/black/rose gold" color scheme of my logo.

really looking for a sleek modern design the breaths professional and artistic.

Target Market(s)

wedding and event films.

Industry/Entity Type

Film Production

Number of Pages Required

5+ page

Colors

Designer to choose colors to be used in the design.

Requirements
Must have
• website name will be www.danemorrowfilms.example
• tagline is "CINEMATIC STORIES ABOUT YOU"
• sections: HOME, CONTACT, ABOUT, FILMS, BLOG
• You can see my old website at danemorrowfilms.example
• Website about section:
• Dane Morrow Films was Established with the basis of truly cinematic and artistic films in mind. Dane and his team routinely travel the globe documenting weddings and events for high profile clients and discerning couples. Dane was born and raised in Maui Hawaii and has a unique approach to his films that embody the essence of a Hollywood film. Dane has spent the last 10 years traveling the world documenting corporate events and weddings with multiple Award winning production companies. In 2017 Dane decided to establish his own brand “Dane Morrow films” that will take everything he has learned with his past experiences and push it to the next level. Aside from his personal achievements, Dane is extremely passionate about his craft and always looks forward to handcrafting beautiful wedding/event films for his clients. The style of work is non-traditional and the day of filming is extremely unobtrusive (as we are looking for natural-candid/ raw emotions).
• If you are looking for the best price in town, we are probably not the best option, but if you’re looking for the best quality and peace of mind on your wedding day, then you’re in the right place. Dane Morrow Films is a boutique studio that only accepts a limited number of assignments per year. Inquire early to ensure availability.
• LINKS TO VIMEO VIDEOS THAT WILL BE IN THE "FILMS' SECTION.
• BRENT FILM TRAILER - https://clipvault.example/508114362
• BRENT FEATURE FILM - https://clipvault.example/617392048
• JUNE AND ROB'S WEDDING - https://clipvault.example/724958160
• DRONE DEMO REEL - https://clipvault.example/841576203
• WEDDING INDUSTRY EVENT PARTY - https://clipvault.example/962304817/a8d3e7b21c
• images that you can use on site are here: https://brigittolsenimages.proofbox.example/gallery/nora&felix/
• password is: meadow

```html
<!DOCTYPE html>
<html lang="en">
<head>
<meta charset="utf-8">
<title>Dane Morrow Films — Cinematic Stories About You</title>
<link rel="stylesheet" href="https://fonts.googleapis.com/css2?family=Open+Sans:wght@400;600;700&family=Roboto+Slab:wght@300;400&family=Dancing+Script:wght@500&display=swap">
<style>
:root{
  --accent:#e8862a;
  --accent-deep:#c9661a;
  --ink:#111;
  --text:#555;
  --muted:#777;
  --paper:#fff;
  --mist:#ececec;
  --night:#262626;
  --night-panel:#353535;
  --hero-a:#3d3a36;
  --hero-b:#1c1b1a;
}
*{margin:0;padding:0;box-sizing:border-box}
html,body{width:1200px;height:4054px;overflow:hidden}
body{position:relative;background:var(--paper);font-family:"Open Sans",Arial,sans-serif;color:var(--text)}
.abs{position:absolute}
.photo{position:absolute;display:block}

/* hero */
.hero{position:absolute;left:0;top:0;width:1200px;height:724px;background:linear-gradient(160deg,#5a5650 0%,var(--hero-a) 40%,var(--hero-b) 100%)}
.brand-tab{position:absolute;left:127px;top:0;width:178px;height:195px}
.brand-tab svg{position:absolute;inset:0}
.brand-tab .brand-name{position:absolute;left:0;top:78px;width:178px;text-align:center;font:600 20px/1.1 "Open Sans",sans-serif;color:var(--ink);letter-spacing:1px}
.menu-icon{position:absolute;left:1040px;top:34px}
.hero-arrow{position:absolute;top:340px}
.tagline{position:absolute;left:197px;top:305px;color:var(--accent);font:300 60px/1 "Roboto Slab",serif}
.tagline-sub{position:absolute;left:200px;top:365px;color:var(--paper);font:500 48px/1 "Dancing Script",cursive}

.mist-band{position:absolute;left:0;top:724px;width:1200px;height:316px;background:var(--mist)}

/* about card */
.about-card{position:absolute;left:127px;top:551px;width:946px;height:422px;background:var(--paper)}
.about-card .photo{left:0;top:0;width:424px;height:422px;background:linear-gradient(180deg,#b9b9b9,#4a4a4a)}
.about-body{position:absolute;left:457px;top:32px;width:460px}
.about-title{font:400 37px/1 "Open Sans",sans-serif;color:var(--ink)}
.about-lead{margin-top:26px;font:700 18px/1.4 "Open Sans",sans-serif;color:var(--accent)}
.about-text{margin-top:14px;font:400 13.5px/1.6 "Open Sans",sans-serif;color:var(--muted)}
.btn-outline{display:inline-block;border:2px solid var(--accent);color:var(--accent);font:400 15px/1 "Roboto Slab",serif;padding:10px 18px;text-transform:uppercase}
.about-body .btn-outline{margin-top:30px}

/* section headings */
.section-title{position:absolute;left:0;width:1200px;text-align:center;font:400 36px/1 "Open Sans",sans-serif;color:var(--ink)}
.section-intro{position:absolute;left:190px;width:820px;text-align:center;font:600 13.5px/1.75 "Open Sans",sans-serif;color:#333}

/* services */
.service{position:absolute;top:1214px;width:208px;height:205px}
.service .photo{inset:0}
.service-label{position:absolute;left:0;bottom:13px;width:100%;height:32px;background:rgba(0,0,0,.45);color:var(--paper);text-align:center;font:400 20px/32px "Roboto Slab",serif;letter-spacing:1px}

/* why band */
.why{position:absolute;left:0;top:1495px;width:1200px;height:513px;background:linear-gradient(180deg,#2d3327,#1f241c 60%,#3a3a30)}
.why-title{position:absolute;left:0;top:48px;width:1200px;text-align:center;font:400 35px/1 "Open Sans",sans-serif;color:var(--paper)}
.feature-hl{position:absolute;left:460px;top:116px;width:281px;height:357px;background:rgba(201,102,26,.88)}
.feature{position:absolute;top:150px;width:281px;text-align:center;color:var(--paper)}
.feature svg{display:block;margin:0 auto;height:82px}
.feature-name{margin-top:20px;font:400 23px/1 "Roboto Slab",serif;letter-spacing:1px}
.feature-text{margin:18px auto 0;width:215px;font:400 13px/1.65 "Open Sans",sans-serif;color:#ddd}
.feature .btn-outline{margin-top:20px;font-size:14px;padding:10px 14px}
.feature .btn-light{border-color:var(--paper);color:var(--paper)}

/* films */
.film{position:absolute;width:462px}
.film .photo{position:relative;width:462px;height:346px}
.film-title{margin-top:22px;font:400 34px/1.1 "Open Sans",sans-serif;color:var(--ink)}
.film-sub{margin-top:6px;font:600 13px/1 "Open Sans",sans-serif;color:#555}

/* enquiry */
.enquiry{position:absolute;left:0;top:3219px;width:1200px;height:600px;background:var(--night)}
.enquiry-note{position:absolute;left:0;top:50px;width:1200px;text-align:center;font:700 18px/1.45 "Open Sans",sans-serif;color:var(--paper)}
.enquiry .photo{left:127px;top:133px;width:554px;height:462px;background:linear-gradient(135deg,#eeeae0,#dcd8cc)}
.form-panel{position:absolute;left:681px;top:133px;width:392px;height:462px;background:var(--night-panel);padding:28px 41px}
.form-title{font:400 33px/1 "Open Sans",sans-serif;color:var(--paper)}
.form-hint{margin-top:10px;font:700 13px/1 "Open Sans",sans-serif;color:var(--paper)}
.field{display:block;width:302px;height:36px;margin-top:10px;background:var(--paper);border:0;padding:0 10px;font:400 12px "Open Sans",sans-serif;color:#999;line-height:36px}
.form-hint+.field{margin-top:18px}
.field-area{height:124px;line-height:1;padding-top:10px}
.btn-solid{display:inline-block;margin-top:14px;background:var(--accent);color:var(--paper);font:600 15px/40px "Open Sans",sans-serif;padding:0 22px;text-transform:uppercase}

/* footer */
.footer-brand{position:absolute;left:127px;top:3948px;font:600 22px/1 "Open Sans",sans-serif;color:var(--ink)}
.footer-nav{position:absolute;right:127px;top:3918px;font:400 14px/1 "Open Sans",sans-serif;color:#333}
.footer-nav .active{color:var(--accent)}
.footer-nav span.sep{margin:0 6px}
.social{position:absolute;left:899px;top:3960px;display:flex;gap:8px}
.social span{width:38px;height:38px;border:2px solid #333;border-radius:3px}
.copyright{position:absolute;right:127px;top:4014px;font:400 13px/1 "Open Sans",sans-serif;color:#333}
</style>
</head>
<body>

<header class="hero">
  <div class="photo" role="img" aria-label="Bride and groom embracing on a rocky coastline at dusk" style="inset:0;background:linear-gradient(100deg,rgba(0,0,0,.1),rgba(0,0,0,.35))"></div>
  <div class="brand-tab">
    <svg width="178" height="195" viewBox="0 0 178 195"><polygon points="0,0 178,0 178,128 0,195" fill="#fff"/></svg>
    <div class="brand-name">Dane Morrow Films</div>
  </div>
  <svg class="menu-icon" width="34" height="24" viewBox="0 0 34 24"><rect y="0" width="34" height="4" fill="#fff"/><rect y="10" width="34" height="4" fill="#fff"/><rect y="20" width="34" height="4" fill="#fff"/></svg>
  <svg class="hero-arrow" style="left:82px" width="16" height="28" viewBox="0 0 16 28"><polyline points="13,2 3,14 13,26" fill="none" stroke="#fff" stroke-width="3"/></svg>
  <svg class="hero-arrow" style="left:1104px" width="16" height="28" viewBox="0 0 16 28"><polyline points="3,2 13,14 3,26" fill="none" stroke="#fff" stroke-width="3"/></svg>
  <h1 class="tagline">Cinematic Stories</h1>
  <div class="tagline-sub">about you</div>
</header>

<div class="mist-band"></div>

<section class="about-card">
  <div class="photo" role="img" aria-label="Black and white portrait of the filmmaker"></div>
  <div class="about-body">
    <h2 class="about-title">DANE MORROW</h2>
    <p class="about-lead">At Dane Morrow Films we specialize in offering the finest in wedding and corporate cinematography.</p>
    <p class="about-text">We offer a very modern and creative style for capturing your special moments with a beautiful and cinematic approach that enables us to produce the highest quality of films. Dane and his hand selected team have over 10 years of experience, and they strive to make the best films in the industry. We pride ourselves on remaining attentive to clients' needs, business practices rooted in integrity, and continually striving to be at the forefront of innovation in our industry.</p>
    <a class="btn-outline">Read more</a>
  </div>
</section>

<h2 class="section-title" style="top:1090px">WHAT WE DO</h2>
<p class="section-intro" style="top:1137px">Aliquam erat volutpat nullam semper, lorem vitae rhoncus consequat, quam dui posuere nunc, nec dignissim arcu nunc quis nibh. Quisque fringilla diam sit amet risus laoreet molestie.</p>

<div class="service" style="left:127px"><div class="photo" role="img" aria-label="Guests gathered at a corporate event" style="background:linear-gradient(160deg,#cfc7bd,#6b4a44)"></div><div class="service-label">CORPORATE</div></div>
<div class="service" style="left:373px"><div class="photo" role="img" aria-label="Groom carrying his bride outdoors" style="background:linear-gradient(160deg,#c7d2dc,#5a5f66)"></div><div class="service-label">WEDDINGS</div></div>
<div class="service" style="left:619px"><div class="photo" role="img" aria-label="Aerial view of an estate garden venue" style="background:linear-gradient(160deg,#b6c2a0,#4d5c3a)"></div><div class="service-label">SPECIAL EVENTS</div></div>
<div class="service" style="left:865px"><div class="photo" role="img" aria-label="Mother and child smiling together" style="background:linear-gradient(160deg,#e8d2b8,#a77f5e)"></div><div class="service-label">SHORT FILMS</div></div>

<section class="why">
  <div class="photo" role="img" aria-label="Wooded hillside venue seen from above" style="inset:0;background:rgba(0,0,0,.25)"></div>
  <h2 class="why-title">WHY CHOOSE DANE MORROW?</h2>
  <div class="feature-hl"></div>
  <div class="feature" style="left:138px">
    <svg width="200" height="82" viewBox="0 0 200 82"><g fill="#fff"><rect x="10" y="8" width="70" height="5" rx="2"/><rect x="120" y="8" width="70" height="5" rx="2"/><rect x="40" y="10" width="6" height="16"/><rect x="154" y="10" width="6" height="16"/><path d="M40 24 H160 L140 44 H60 Z"/><rect x="84" y="44" width="32" height="8"/><circle cx="100" cy="64" r="14"/></g><circle cx="100" cy="64" r="6" fill="#2b2f27"/><path d="M70 44 L58 70 M130 44 L142 70" stroke="#fff" stroke-width="4"/></svg>
    <div class="feature-name">CREATIVE</div>
    <p class="feature-text">Donec et tempus ex donec at nisi auctor, semper ante aliquet aliquam leo. Integer aliquam tellus nulla, et pharetra tellus facilisis dapibus.</p>
    <a class="btn-outline">Learn more</a>
  </div>
  <div class="feature" style="left:460px">
    <svg width="70" height="82" viewBox="0 0 70 82"><g fill="#fff"><circle cx="35" cy="30" r="26"/><path d="M18 50 L10 80 L22 72 L28 82 L35 56 Z M52 50 L60 80 L48 72 L42 82 L35 56 Z"/></g><circle cx="35" cy="30" r="17" fill="none" stroke="#c9661a" stroke-width="3"/><polygon points="35,19 38,27 46,27 40,32 42,40 35,35 28,40 30,32 24,27 32,27" fill="#c9661a"/></svg>
    <div class="feature-name">QUALITY</div>
    <p class="feature-text">Aliquam erat volutpat nullam semper, lorem vitae rhoncus consequat, quam dui posuere nunc, nec dignissim arcu nunc quis nibh.</p>
    <a class="btn-outline btn-light">Learn more</a>
  </div>
  <div class="feature" style="left:787px">
    <svg width="70" height="82" viewBox="0 0 70 82"><g fill="#fff"><rect x="6" y="36" width="14" height="36" rx="2"/><path d="M24 38 L38 12 C42 6 50 8 48 16 L44 32 H60 C66 32 68 38 64 42 C68 46 66 52 62 53 C65 57 62 62 58 63 C60 68 56 72 52 72 H24 Z"/></g></svg>
    <div class="feature-name">SATISFACTION</div>
    <p class="feature-text">Maecenas rhoncus vulputate est, a finibus nisi posuere quisque vitae, commodo mauris posuere tincidunt non lorem ac porta.</p>
    <a class="btn-outline">Learn more</a>
  </div>
</section>

<h2 class="section-title" style="top:2054px">FILMS</h2>
<p class="section-intro" style="top:2114px">Aliquam erat volutpat nullam semper, lorem vitae rhoncus consequat, quam dui posuere nunc, nec dignissim arcu nunc quis nibh. Quisque fringilla diam sit amet risus laoreet molestie.</p>

<article class="film" style="left:127px;top:2198px">
  <div class="photo" role="img" aria-label="Groom lifting his bride on a seaside cliff" style="background:linear-gradient(160deg,#a9b59a,#5d6b57 60%,#8a8576)"></div>
  <h3 class="film-title">B R E N T - FILM TRAILER</h3>
  <p class="film-sub">FUSCE TRISTIQUE CONVALLIS</p>
</article>
<article class="film" style="left:611px;top:2198px">
  <div class="photo" role="img" aria-label="Bride and groom smiling among wedding guests" style="background:linear-gradient(160deg,#9fb08a,#6a7a5c 55%,#2c3850)"></div>
  <h3 class="film-title">B R E N T - FEATURE FILM</h3>
  <p class="film-sub">FUSCE TRISTIQUE CONVALLIS</p>
</article>
<article class="film" style="left:127px;top:2687px">
  <div class="photo" role="img" aria-label="Couple sharing a kiss wearing flower leis" style="background:linear-gradient(160deg,#6d7a4a,#3f4a2b 55%,#b5906e)"></div>
  <h3 class="film-title">JUNE AND ROB’S WEDDING</h3>
  <p class="film-sub">FUSCE TRISTIQUE CONVALLIS</p>
</article>
<article class="film" style="left:611px;top:2687px">
  <div class="photo" role="img" aria-label="Mountain peaks above an alpine lake" style="background:linear-gradient(180deg,#7ea3d0 0%,#b9c4cc 30%,#5c6a4a 62%,#3f6b6a 100%)"></div>
  <h3 class="film-title">MAUI &amp; ASPEN TONECRAFT<br>REEL - 2015</h3>
  <p class="film-sub">FUSCE TRISTIQUE CONVALLIS</p>
</article>

<section class="enquiry">
  <p class="enquiry-note">Dane Morrow Films is a boutique studio that only accepts a limited number of assignments per year.<br>Inquire early to ensure availability.</p>
  <div class="photo" role="img" aria-label="Road map of the studio's service region"></div>
  <form class="form-panel">
    <h2 class="form-title">ENQUIRY FORM</h2>
    <p class="form-hint">Please fill the form below</p>
    <span class="field">Full Name</span>
    <span class="field">Email</span>
    <span class="field">Phone</span>
    <span class="field field-area">Description</span>
    <span class="btn-solid">Enquire now</span>
  </form>
</section>

<footer>
  <div class="footer-brand">Dane Morrow Films</div>
  <nav class="footer-nav"><span class="active">HOME</span><span class="sep">|</span>ABOUT<span class="sep">|</span>FILMS<span class="sep">|</span>BLOG<span class="sep">|</span>CONTACT</nav>
  <div class="social" aria-label="Social links"><span></span><span></span><span></span><span></span></div>
  <p class="copyright">Copyright © 2017 danemorrowfilms.example. All rights reserved.</p>
</footer>

</body>
</html>
```